Design NEW business card

We would like a business card using the colour deep red wine or dark navy blue textured background (patterned or not, open to suggestions) with a high gloss debossed rose gold/copper MT Martin Tully Jewellery business name (Provided). I have included images for your review we would like to keep our currently logo and business name on the front but you can change the layout and positioning. For the back of the card we are open to all suggestions/variations.
Industry/Entity Type
Business
Contact Information for Business Card
Use our current MT Martin Tully Jewellery logo (Provided image)
Look and feel
Each slider illustrates characteristics of the customer's brand and the style your logo design should communicate.

```html
<!DOCTYPE html>
<html lang="en">
<head>
<meta charset="utf-8">
<title>Martin Tully Jewellery – Business Cards</title>
<link rel="stylesheet" href="https://fonts.googleapis.com/css2?family=Montserrat:wght@400&family=Source+Sans+3:wght@300;400&display=swap">
<style>
  :root {
    --backdrop: #d5b48f;
    --card-wine: #561c24;
    --rose-gold: #c27a8c;
    --contact-text: #c99ea6;
  }
  * { margin: 0; padding: 0; box-sizing: border-box; }
  html, body {
    width: 1200px;
    height: 1200px;
    overflow: hidden;
    background: var(--backdrop);
  }
  .canvas {
    position: relative;
    width: 1200px;
    height: 1200px;
  }
  .card {
    position: absolute;
    left: 310px;
    width: 583px;
    height: 332px;
    background: var(--card-wine);
  }
  .card--front { top: 214px; }
  .card--back { top: 626px; }

  .monogram {
    position: absolute;
    display: flex;
    align-items: center;
    justify-content: center;
    border: 1.5px solid var(--rose-gold);
    border-radius: 50%;
    font-family: "Montserrat", sans-serif;
    font-weight: 400;
    color: var(--rose-gold);
    letter-spacing: 2px;
  }
  .card--front .monogram { left: 150px; top: 84px; width: 100px; height: 100px; font-size: 30px; }
  .card--back .monogram { left: 162px; top: 76px; width: 90px; height: 90px; font-size: 27px; }

  .brand-name {
    position: absolute;
    font-family: "Montserrat", sans-serif;
    font-weight: 400;
    color: var(--rose-gold);
    white-space: nowrap;
  }
  .brand-name__primary {
    display: block;
    font-size: 22px;
    letter-spacing: 6px;
  }
  .brand-name__secondary {
    display: block;
    margin-top: 12px;
    font-size: 9px;
    letter-spacing: 22.5px;
  }
  .card--front .brand-name { left: 212px; top: 200px; }
  .card--back .brand-name { left: 214px; top: 190px; }
  .card--back .brand-name__primary { font-size: 20px; letter-spacing: 5.5px; }
  .card--back .brand-name__secondary { margin-top: 10px; font-size: 8px; letter-spacing: 20px; }

  .holder {
    position: absolute;
    left: 38px;
    top: 262px;
    font-family: "Source Sans 3", sans-serif;
    font-weight: 300;
    color: var(--contact-text);
  }
  .holder__name { font-size: 16px; letter-spacing: 0.4px; }
  .holder__role { font-size: 12.5px; margin-top: 2px; }

  .contact-list {
    position: absolute;
    right: 46px;
    top: 249px;
    list-style: none;
    text-align: right;
    font-family: "Source Sans 3", sans-serif;
    font-weight: 300;
    font-size: 12px;
    line-height: 18.5px;
    color: var(--contact-text);
  }
</style>
</head>
<body>
<main class="canvas">
  <section class="card card--front" aria-label="Card front">
    <div class="monogram">MT</div>
    <div class="brand-name">
      <span class="brand-name__primary">MARTIN TULLY</span>
      <span class="brand-name__secondary">JEWELLERY</span>
    </div>
  </section>

  <section class="card card--back" aria-label="Card back">
    <div class="monogram">MT</div>
    <div class="brand-name">
      <span class="brand-name__primary">MARTIN TULLY</span>
      <span class="brand-name__secondary">JEWELLERY</span>
    </div>
    <div class="holder">
      <p class="holder__name">Your Full Name</p>
      <p class="holder__role">Designation</p>
    </div>
    <ul class="contact-list">
      <li>(03)+ 55-210-947</li>
      <li>info@mtjewellers.com</li>
      <li>www.mtjewellers.com</li>
    </ul>
  </section>
</main>
</body>
</html>
```